Orbit Cheerleading flyer for new recreational cheerleading classes starting in Term 4

I am looking for a flyer to advertise recreational cheerleading classes starting in Term 4. The flyer would need to include the details which are:

For ages 6 -12 years
Monday nights 5pm - 6pm
Starting 10 October 2016

For ages 13 - 18 year
Wednesday nights 7pm - 8pm
Starting 12 October 2016

Classes take place at Unit 4/9 Wexley Lane Mitchell ACT 2905. Cost is $150 for the term

I've attached a copy of a flyer that I really like, the Orbit Cheerleading log and some photos that might be helpful. Our colours are red, black and gold, so I would like those colours incorporated in the flyer please.

Target Market(s)

Girls and boys from 6 years to 18 years

Font styles to use
Sans Serif
Other font styles liked:
• Philly Sans

Colors
f04a50
fece3e
ffffff

Requirements
Must have
• Recreational class details included
• Orbit Logo

```html
<!DOCTYPE html>
<html lang="en">
<head>
<meta charset="utf-8">
<title>Orbit Cheerleading – Term 4 Classes</title>
<link href="https://fonts.googleapis.com/css2?family=Anton&family=Oswald:wght@500;700&family=Open+Sans:wght@600&display=swap" rel="stylesheet">
<style>
  :root {
    --red: #e3232b;
    --red-bright: #f04a50;
    --gold: #fece3e;
    --gold-deep: #f5b400;
    --black: #111111;
    --white: #ffffff;
    --page: #3a3a3a;
    --paper-light: #f4f4f4;
    --paper-mid: #d9d9d9;
  }
  * { box-sizing: border-box; margin: 0; padding: 0; }
  html, body {
    width: 980px; height: 1200px; overflow: hidden;
    background: var(--page);
  }
  .flyer {
    position: absolute; left: 90px; top: 32px;
    width: 800px; height: 1136px; overflow: hidden;
    background: radial-gradient(circle at 60% 30%, var(--paper-light) 0%, var(--paper-mid) 70%, #c9c9c9 100%);
    font-family: "Oswald", sans-serif;
  }
  .logo-banner {
    position: absolute; left: 71px; top: 0; width: 155px; height: 265px;
    background: var(--red);
    clip-path: polygon(0 0, 100% 0, 100% 100%, 50% 88%, 0 100%);
    display: flex; flex-direction: column; align-items: center; justify-content: center;
    gap: 10px; padding-bottom: 30px;
  }
  .logo-dot { width: 22px; height: 22px; border-radius: 50%; background: var(--gold); }
  .logo-name {
    font-family: "Oswald", sans-serif; font-weight: 700; font-size: 24px; line-height: 1.05;
    color: var(--gold); text-align: center; text-transform: uppercase;
  }
  .headline {
    position: absolute; left: 420px; top: 40px; width: 350px; text-align: center;
  }
  .headline-line {
    font-family: "Oswald", sans-serif; font-weight: 700; font-size: 37px; line-height: 44px;
    color: var(--red); text-transform: uppercase;
  }
  .headline-key {
    font-family: "Anton", sans-serif; font-size: 96px; line-height: 104px;
    color: var(--black); letter-spacing: 2px;
  }
  .photo {
    position: absolute; border-radius: 50%;
    border: 9px solid var(--black);
    box-shadow: inset 0 0 0 4px var(--red), 0 6px 14px rgba(0,0,0,.35);
  }
  .photo-team {
    left: 71px; top: 284px; width: 322px; height: 322px;
    background: radial-gradient(circle at 50% 35%, #9a5cc8 0%, #5a2f86 55%, #2c1740 100%);
  }
  .photo-stunt {
    left: 397px; top: 255px; width: 226px; height: 226px;
    background: radial-gradient(circle at 50% 40%, #b078d8 0%, #6c3ca0 60%, #3a1f58 100%);
  }
  .photo-flyer {
    left: 90px; top: 638px; width: 284px; height: 284px;
    background: radial-gradient(circle at 50% 40%, #d44a78 0%, #8a2c7a 55%, #3b1646 100%);
  }
  .wave { position: absolute; left: 0; top: 800px; width: 800px; height: 336px; }
  .class-badge {
    position: absolute; width: 206px; height: 206px; border-radius: 50%;
    border: 9px solid var(--black);
    display: flex; flex-direction: column; align-items: center; justify-content: center;
    text-align: center; text-transform: uppercase; line-height: 1.05;
    box-shadow: 0 6px 14px rgba(0,0,0,.3);
  }
  .class-junior { left: 516px; top: 529px; background: var(--red); color: var(--white); }
  .class-senior { left: 523px; top: 723px; background: var(--gold); color: var(--black); }
  .badge-label { font-weight: 700; font-size: 30px; }
  .badge-ages { font-weight: 700; font-size: 34px; margin-bottom: 8px; }
  .badge-time { font-weight: 500; font-size: 14px; text-transform: none; margin-bottom: 8px; }
  .badge-start { font-weight: 700; font-size: 20px; }
  .badge-date { font-weight: 700; font-size: 16px; }
  .cost-box {
    position: absolute; left: 393px; top: 978px; width: 358px; height: 90px;
    background: var(--gold); border-radius: 10px; padding: 6px;
    box-shadow: 0 6px 12px rgba(0,0,0,.35);
  }
  .cost-inner {
    width: 100%; height: 100%; border: 2px dashed var(--gold-deep); border-radius: 7px;
    display: flex; align-items: center; justify-content: space-between; padding: 0 16px;
    color: var(--black);
  }
  .cost-label { font-family: "Anton", sans-serif; font-size: 36px; line-height: 36px; }
  .cost-term { display: block; font-family: "Oswald", sans-serif; font-weight: 700; font-size: 18px; line-height: 20px; }
  .cost-amount { font-family: "Anton", sans-serif; font-size: 60px; line-height: 60px; }
  .contact {
    position: absolute; left: 58px; display: flex; align-items: center; gap: 12px;
    font-family: "Open Sans", sans-serif; font-weight: 600; color: var(--white);
  }
  .contact-phone { top: 1022px; font-size: 20px; }
  .contact-web { top: 1056px; font-size: 17px; }
  .contact svg { width: 20px; height: 20px; }
  .venue {
    position: absolute; left: 58px; top: 1094px;
    font-family: "Open Sans", sans-serif; font-weight: 600; font-size: 19px; color: var(--gold);
  }
</style>
</head>
<body>
<main class="flyer">
  <div class="logo-banner">
    <span class="logo-dot"></span>
    <span class="logo-name">Orbit<br>Cheerleading</span>
  </div>

  <header class="headline">
    <p class="headline-line">If it's in your heart</p>
    <p class="headline-line">it shows in your</p>
    <p class="headline-key">SPIRIT</p>
  </header>

  <div class="photo photo-team" role="img" aria-label="Photo of the cheer team performing a group pyramid on stage"></div>
  <div class="photo photo-stunt" role="img" aria-label="Photo of a coach beside two cheerleaders doing a lift"></div>

  <svg class="wave" viewBox="0 0 800 336" aria-hidden="true">
    <path d="M0,40 C220,70 430,150 800,70 L800,336 L0,336Z" fill="var(--gold)"/>
    <path d="M0,62 C220,92 430,170 800,88 L800,336 L0,336Z" fill="var(--black)"/>
    <path d="M0,76 C220,106 430,186 800,102 L800,336 L0,336Z" fill="var(--red)"/>
  </svg>

  <div class="photo photo-flyer" role="img" aria-label="Photo of a young cheerleader held up in a stunt"></div>

  <section class="class-badge class-junior">
    <span class="badge-label">For ages</span>
    <span class="badge-ages">6 -12 years</span>
    <span class="badge-time">Monday Nights 5pm - 6pm</span>
    <span class="badge-start">Starting</span>
    <span class="badge-date">10 October 2016</span>
  </section>

  <section class="class-badge class-senior">
    <span class="badge-label">For ages</span>
    <span class="badge-ages">13 -18 years</span>
    <span class="badge-time">Wednesday Nights 7pm - 8pm</span>
    <span class="badge-start">Starting</span>
    <span class="badge-date">12 October 2016</span>
  </section>

  <div class="cost-box">
    <div class="cost-inner">
      <span class="cost-label">Cost is<span class="cost-term">For The Term</span></span>
      <span class="cost-amount">$150</span>
    </div>
  </div>

  <p class="contact contact-phone">
    <svg viewBox="0 0 24 24" aria-hidden="true"><circle cx="12" cy="12" r="10.5" fill="none" stroke="var(--gold)" stroke-width="2"/><path d="M8.5 6.5l2 2-1.2 1.5c.7 1.6 1.9 2.8 3.5 3.5l1.5-1.2 2 2-1.3 1.6c-3.8-.4-7.7-4.3-8.1-8.1z" fill="var(--gold)"/></svg>
    0400 318 526
  </p>
  <p class="contact contact-web">
    <svg viewBox="0 0 24 24" aria-hidden="true"><g fill="none" stroke="var(--gold)" stroke-width="2"><circle cx="12" cy="12" r="10"/><ellipse cx="12" cy="12" rx="4" ry="10"/><path d="M2 12h20"/></g></svg>
    www.orbitcheerclub.com
  </p>
  <p class="venue">Classes take place at - Unit 4/9 Wexley Lane Mitchell ACT 2905.</p>
</main>
</body>
</html>
```